Clothes Pop-art web site "Kindred"

Hello,

its a pop art t-shirt company we appreciate islamic art and arabic heritage
i need a web design that represent my company and offer easy sale platform , i attached some logo sample.

My basic site map will include;
-About
-Kindred look book
-Kindred friends- 4 roots
-shop-2 roots Kindred product-other brand product
-contact-Insta-Twiiter-FB-Email
-bog via Tumbler

also i attached my busniess card i would like to to have Instgram-twitter-face book links via the contact root including my email address

My Terms:
-Less SENSELESS SCROLLING
-ALWAYS RESPONSIVE
The general tendency to be entirely responsive across all mobile, tablet and desktop devices. Mobile Friendly Friendly"
Content carousels;
Overly large hero images;
Overused stock photos;
Autoplay videos;
Automated popups;
Advertising sidebars;
“Hello world” blog posts;
Reloading pages;
Modal windows with hidden or tiny close commands;
Loading screens;
Small font sizes;
Long shadows;
Hipster icons and logos.

some website example i like :
http://qv-atelier.example
http://lorimpress.example/home
http://pixmorra.example/design/web-illus/illustration-website-design/25/15/tkvalde.example/jpg/s?nid=7206http://pixmorra.example/pixmorra/blog/25-beautiful-and-creative-illustration-themed-web-design-examples

my Main color theme :PANTONE :13-4909 Light Blue

Good Luck

Reason: not much involving

Reason: i dont like any design

Target Market(s)

teen
youth
unisex

Industry/Entity Type

It Company

Coding

Coded - Design and coding required

Number of Pages Required

3 page

Colors
86cfc6
85cae6
33b8a4
33a6d7
00a990
0792cd

Requirements
Must have
• color theme :PANTONE :13-4909 Light Blue
• arabic calligraphy Ultra modern
• islamic ART patterns ULTRA Modern
Nice to have
• Content carousels;
• Overly large hero images;
• Overused stock photos;
• Autoplay videos;
• Automated popups;
• Advertising sidebars;
• “Hello world” blog posts;
• Reloading pages;
• Modal windows with hidden or tiny close commands;
• Loading screens;
• Small font sizes;
• Long shadows;
• Hipster icons and logos.

```html
<!DOCTYPE html>
<html lang="en">
<head>
<meta charset="utf-8">
<title>Kindred — Pop Art T-shirts</title>
<link rel="stylesheet" href="https://fonts.googleapis.com/css2?family=Montserrat:wght@600;700&family=Roboto:wght@400;500&display=swap">
<style>
:root{
  --ink:#0d0d0d;
  --header:#1d1d1d;
  --footer:#1a1a1a;
  --teal:#1f9e8e;
  --teal-deep:#0f3d4a;
  --sky:#5ab4d6;
  --accent:#33b8a4;
  --white:#ffffff;
  --muted:#d9d9d9;
  --play:#c74a0c;
}
*{margin:0;padding:0;box-sizing:border-box}
html,body{width:1132px;height:1200px;overflow:hidden;background:var(--ink)}
body{position:relative;font-family:"Roboto",sans-serif;color:var(--white)}
.abs{position:absolute}
.photo{display:block}

.site-header{left:0;top:0;width:1132px;height:135px;background:var(--header)}
.brand{left:31px;top:44px;font-weight:500;font-size:38px;color:var(--sky);letter-spacing:1px}
.main-nav{left:508px;top:65px;font-weight:500;font-size:10px}
.main-nav a{position:absolute;color:var(--white);text-decoration:none;white-space:nowrap}
.main-nav a.active{color:var(--accent)}

.hero{left:0;top:135px;width:724px;height:512px;background:var(--teal)}
.hero-title{left:342px;top:143px;font-family:"Montserrat",sans-serif;font-weight:700;font-size:32px;line-height:38px;color:#111}
.hero-copy{left:344px;top:265px;width:318px;font-size:10.5px;line-height:19.4px;color:#1a1a1a}

.btn{display:flex;align-items:center;justify-content:center;font-family:"Montserrat",sans-serif;font-weight:700;font-size:11.5px;color:var(--white);border:1px solid var(--white);text-decoration:none}
.dots{display:flex;gap:4px}
.dots span{width:13px;height:13px;border-radius:50%;background:#6d6d6d}
.dots span.on{background:var(--white)}
.dots.small span{width:9px;height:9px}
.play{width:32px;height:32px;border-radius:50%;background:var(--play);display:flex;align-items:center;justify-content:center}

.tile-title{font-family:"Montserrat",sans-serif;font-weight:700;color:var(--white)}
.big-title{font-family:"Montserrat",sans-serif;font-weight:700;font-size:32px;line-height:38px}
.body-copy{font-size:10.5px;line-height:19.4px}

.site-footer{left:0;top:1100px;width:1132px;height:100px;background:var(--footer)}
.footer-links{left:93px;top:24px;font-size:10.5px;color:var(--muted);white-space:nowrap}
.footer-links span{margin-right:6px}
.social{left:92px;top:51px;display:flex;gap:3px}
.social a{width:27px;height:27px;border-radius:50%;border:1.5px solid #9a9a9a;display:block;background:#242424}
.footer-brand{left:557px;top:33px;font-size:27px;font-weight:500;color:var(--white);letter-spacing:1px}
.copyright{left:723px;top:41px;font-size:10.5px;color:var(--muted);white-space:nowrap}
.page-code{left:1078px;top:41px;font-size:10.5px;color:var(--muted)}
</style>
</head>
<body>

<header class="abs site-header">
  <div class="abs brand">Kindred</div>
  <nav class="abs main-nav">
    <a class="active" style="left:0">HOME</a>
    <a style="left:58px">ABOUT</a>
    <a style="left:121px">KINDRED LOOKBOOK</a>
    <a style="left:251px">KINDRED FRIENDS</a>
    <a style="left:369px">SHOP</a>
    <a style="left:425px">CONTACT</a>
    <a style="left:501px">BLOG</a>
  </nav>
</header>

<section class="abs hero">
  <div class="abs photo" role="img" aria-label="Smiling woman in a white printed T-shirt pointing at the headline" style="left:84px;top:62px;width:200px;height:450px;background:radial-gradient(ellipse 70% 40% at 50% 45%,#f4f6f5 0%,#e6ecea 60%,rgba(230,236,234,0) 100%),linear-gradient(180deg,rgba(31,158,142,0) 0%,rgba(31,158,142,0) 70%,#1c2b2a 100%)"></div>
  <h1 class="abs hero-title">WE ARE CREATING<br>IN AN ARABIC FLAIR<br>&amp; HERITAGE.</h1>
  <p class="abs hero-copy">Lorem Ipsum is simply dummy text of the printing and typesetting industry. Lorem Ipsum has been the industry’s standard dummy text ever since the 1500s.</p>
  <a class="abs btn" style="left:346px;top:344px;width:144px;height:41px">VIEW MORE INFO</a>
  <div class="abs dots" style="left:361px;top:474px"><span></span><span></span><span class="on"></span></div>
</section>

<div class="abs photo" role="img" aria-label="Hand pointing at a white T-shirt with a tiger print" style="left:724px;top:135px;width:408px;height:116px;background:linear-gradient(180deg,#f2f2f2,#e4e4e4)"></div>
<div class="abs photo" role="img" aria-label="Two men in grey T-shirts with pop-art portrait prints" style="left:724px;top:251px;width:408px;height:261px;background:linear-gradient(180deg,#6e6b68 0%,#5b5855 70%,#2c2e35 100%)"></div>
<div class="abs dots small" style="left:765px;top:482px"><span></span><span></span><span class="on"></span></div>
<div class="abs photo" role="img" aria-label="Smiling man in a light sweater with a comic print, video still" style="left:724px;top:512px;width:408px;height:135px;background:linear-gradient(90deg,#d9e3ee,#eef1f5 60%,#cfd8e4)"></div>
<div class="abs play" style="left:902px;top:573px"><svg width="12" height="14" viewBox="0 0 12 14"><path d="M1 0 L12 7 L1 14 Z" fill="#fff"/></svg></div>

<section class="abs" style="left:0;top:647px;width:441px;height:134px;background:var(--teal-deep)">
  <div class="abs photo" role="img" aria-label="Woman in a red pop-art T-shirt" style="left:290px;top:0;width:151px;height:134px;background:linear-gradient(180deg,rgba(15,61,74,0) 0%,rgba(15,61,74,0) 35%,#c9242b 60%,#b01d22 100%)"></div>
  <h2 class="abs tile-title" style="left:93px;top:39px;font-size:19px;line-height:22px">Sed ut perspiciatis<br>unde omnis iste</h2>
</section>

<section class="abs" style="left:0;top:781px;width:441px;height:319px;background:var(--ink)">
  <h2 class="abs big-title" style="left:91px;top:46px">SED UT PERSPIC<br>UNDE OMN ISTE<br>NATUS ERROR</h2>
  <p class="abs body-copy" style="left:94px;top:170px;width:310px">Lorem Ipsum is simply dummy text of the printing and typesetting industry. Lorem Ipsum has been the industry’s standard dummy text ever since the 1500s.</p>
  <a class="abs btn" style="left:95px;top:246px;width:144px;height:41px">VIEW MORE INFO</a>
</section>

<div class="abs photo" role="img" aria-label="Two women in orange and white printed T-shirts, video still" style="left:441px;top:647px;width:252px;height:239px;background:linear-gradient(90deg,#f3f3f3 0%,#d5621c 8%,#cc561a 48%,#f6f6f6 56%,#eeeeee 100%)"></div>
<div class="abs play" style="left:554px;top:759px"><svg width="12" height="14" viewBox="0 0 12 14"><path d="M1 0 L12 7 L1 14 Z" fill="#fff"/></svg></div>

<section class="abs" style="left:441px;top:886px;width:252px;height:214px;background:linear-gradient(135deg,#0f3d4a 0%,#2a7a78 50%,#6fbfa6 100%)">
  <div class="abs photo" role="img" aria-label="Woman in a blue T-shirt with a comic burst print" style="left:0;top:0;width:105px;height:214px;background:linear-gradient(180deg,rgba(15,61,74,0) 0%,#2f66c9 38%,#1f56b8 82%,#141a28 100%)"></div>
  <h2 class="abs tile-title" style="left:110px;top:58px;font-size:17.5px;line-height:22px">Sed ut perspici<br>Atis unde omn<br>is iste</h2>
</section>

<section class="abs" style="left:693px;top:647px;width:439px;height:95px;background:#0a0606">
  <div class="abs photo" role="img" aria-label="White T-shirt with a heart pattern print" style="left:25px;top:16px;width:60px;height:66px;background:#efefef;border-radius:6px"></div>
  <h2 class="abs tile-title" style="left:99px;top:20px;font-size:19px;line-height:22px">Sed ut perspiciatis unde<br>omnis iste</h2>
</section>

<div class="abs photo" role="img" aria-label="Bearded man in a white T-shirt with an ornamental print" style="left:693px;top:742px;width:439px;height:214px;background:radial-gradient(ellipse 30% 70% at 70% 80%,#f4f4f4 0%,#e8e8e8 50%,rgba(190,188,184,0) 100%),linear-gradient(180deg,#b8b5b0,#c6c3be)"></div>

<section class="abs" style="left:693px;top:956px;width:439px;height:144px;background:var(--white);color:#111">
  <svg class="abs" style="left:69px;top:-12px" width="24" height="12" viewBox="0 0 24 12"><path d="M0 12 L12 0 L24 12 Z" fill="#fff"/></svg>
  <h2 class="abs" style="left:24px;top:21px;font-family:'Montserrat',sans-serif;font-weight:700;font-size:18px;line-height:22px">WE ARE CREATING IN AN ARABIC<br>&nbsp;FLAIR &amp; HERITAGE.</h2>
  <p class="abs body-copy" style="left:27px;top:67px;width:310px;color:#222">Lorem Ipsum is simply dummy text of the printing and typesetting industry. Lorem Ipsum has been the industry’s standard dummy text ever since the 1500s, when an unknown printer</p>
</section>

<footer class="abs site-footer">
  <div class="abs footer-links"><span>Privacy Policy |</span><span>Store Locator |</span><span>Advanced Search |</span><span>Terms &amp; Conditions</span></div>
  <nav class="abs social" aria-label="Social links"><a aria-label="Social link 1"></a><a aria-label="Social link 2"></a><a aria-label="Social link 3"></a><a aria-label="Social link 4"></a><a aria-label="Social link 5"></a></nav>
  <div class="abs footer-brand">Kindred</div>
  <p class="abs copyright">Copyrights © 2015 Pop Art T-shirt company . All rights reserved.</p>
  <p class="abs page-code">C12</p>
</footer>

</body>
</html>
```